Unique business card design

We are looking for a design that reflects our unique social media and online marketing agency "Kelvora Media". We are a young agency with a focus on speakers, coaches and trainers. In other words, we support people who want to do good with their work and help other people live a happier, more successful and fulfilling life, reach as many people as possible with their work and thus have an influence. Our values are: sustainability, creating added value, individuality, proactivity. We want our clients to feel comfortable with us and that's why the relationship with them is very important to us. We want every customer to become a lifelong friend of the company. Most of our clients are premium coaches, meaning they are in the higher priced segment and expect seriousness, professionalism and quality. All of these things should reflect our business card as well. I look forward to feedback. Best regards, Dorian Whitcombe
Look and feel
Each slider illustrates characteristics of the customer's brand and the style your logo design should communicate.

```html
<!DOCTYPE html>
<html lang="de">
<head>
<meta charset="utf-8">
<title>Kelvora Media – Visitenkarte</title>
<link rel="stylesheet" href="https://fonts.googleapis.com/css2?family=Quicksand:wght@500;700&family=Open+Sans:wght@400&family=Didact+Gothic&display=swap">
<style>
  :root {
    --bg: #1e1f24;
    --paper: #ffffff;
    --navy: #1f1a63;
    --blue: #1f6fc0;
    --royal: #2a3ea8;
    --grey-light: #b7c0cc;
    --grey: #8a96a6;
    --icon: #9aa2ad;
    --text: #2b3a67;
  }
  * { margin: 0; padding: 0; box-sizing: border-box; }
  html, body { width: 1200px; height: 1200px; overflow: hidden; background: var(--bg); }
  .canvas { position: relative; width: 1200px; height: 1200px; }

  .card {
    position: absolute;
    width: 560px;
    height: 320px;
    background: var(--paper);
  }
  .card--front { left: 80px; top: 200px; }
  .card--back  { left: 560px; top: 660px; }

  .brand {
    position: absolute;
    display: flex;
    align-items: center;
    gap: 12px;
    font-family: "Quicksand", sans-serif;
    font-weight: 700;
    font-size: 30px;
    color: var(--navy);
    letter-spacing: 0.2px;
  }
  .brand__mark { width: 34px; height: 34px; background: var(--navy); flex: none; }
  .card--front .brand { left: 60px; top: 200px; }
  .card--back .brand  { left: 60px; top: 200px; }

  .contact { position: absolute; left: 300px; top: 58px; }
  .contact__name {
    font-family: "Quicksand", sans-serif;
    font-weight: 700;
    font-size: 23px;
    color: var(--blue);
    margin-bottom: 10px;
  }
  .contact__line {
    display: flex;
    align-items: center;
    gap: 8px;
    font-family: "Open Sans", sans-serif;
    font-size: 13.5px;
    color: var(--text);
    line-height: 21px;
  }
  .contact__line svg { width: 13px; height: 13px; fill: var(--icon); flex: none; }

  .values {
    position: absolute;
    right: 46px;
    top: 70px;
    text-align: right;
    font-family: "Didact Gothic", sans-serif;
    font-size: 20px;
    line-height: 27px;
    list-style: none;
  }
  .values__item--1 { color: var(--grey-light); }
  .values__item--2 { color: var(--grey); }
  .values__item--3 { color: var(--blue); }
  .values__item--4 { color: var(--navy); }
</style>
</head>
<body>
<main class="canvas">
  <section class="card card--front">
    <div class="brand"><span class="brand__mark"></span>Kelvora Media</div>
    <div class="contact">
      <p class="contact__name">Dorian Whitcombe</p>
      <p class="contact__line">
        <svg viewBox="0 0 24 24" aria-hidden="true"><path d="M6.6 10.8a15.1 15.1 0 0 0 6.6 6.6l2.2-2.2c.3-.3.7-.4 1-.2 1.1.4 2.3.6 3.6.6.6 0 1 .4 1 1V20c0 .6-.4 1-1 1A17 17 0 0 1 3 4c0-.6.4-1 1-1h3.5c.6 0 1 .4 1 1 0 1.3.2 2.5.6 3.6.1.3 0 .7-.2 1z"/></svg>
        (555) 014 2368
      </p>
      <p class="contact__line">
        <svg viewBox="0 0 24 24" aria-hidden="true"><path d="M2 5h20v14H2zM3.5 6.5v.4L12 12.5l8.5-5.6v-.4z"/></svg>
        hello@kelvoramedia.com
      </p>
      <p class="contact__line">
        <svg viewBox="0 0 24 24" aria-hidden="true"><path d="M12 2a10 10 0 1 0 0 20 10 10 0 0 0 0-20zm-1 6h2v5h3l-4 4-4-4h3z"/></svg>
        kelvoramedia.com
      </p>
    </div>
  </section>

  <section class="card card--back">
    <div class="brand"><span class="brand__mark"></span>Kelvora Media</div>
    <ul class="values">
      <li class="values__item--1">Nachhaltigkeit</li>
      <li class="values__item--2">Mehrwert schaffen</li>
      <li class="values__item--3">Individualität</li>
      <li class="values__item--4">Proaktivität.</li>
    </ul>
  </section>
</main>
</body>
</html>
```